Jahreskalender 2019 / Wandkalender für Foto- und Videoagentur
Immer wieder gern.
Zielgruppe
Wir sind eine Foto und Videoagentur für Nachrichtenthemen in Deutschland. Unser Wandkalender ist für Kunden und Einsatzkräfte.
Aufgabenstellung
Der Wandkalender 2019 soll im Format DIN A1 (84 x 59,4 cm) gedruckt werden. Sie bekommen von uns Fotos und diese müssen gut bearbeitet in den Wandkalender eingefügt werden. Ein Kameramann muss ausgeschnitten werden und etwas dominant im Kalender vorkommen. Sie bekommen zur Ansicht die alten Kalender. Es sollten alle wichtigen Feiertrage im Kalender vorkommen. Auch die Info Box wie in den anderen Kalender muss wieder eingefügt werden.

```html
<!DOCTYPE html>
<html lang="de">
<head>
<meta charset="utf-8">
<title>Wandkalender 2019 – PRESSE7</title>
<link href="https://fonts.googleapis.com/css2?family=Oswald:wght@500;700&family=Roboto+Condensed:wght@400;700&display=swap" rel="stylesheet">
<style>
:root{
  --smoke-dark:#2b3133;
  --smoke-mid:#5d6667;
  --fire:#d8641e;
  --paper:#ffffff;
  --weekend:#dfe9ad;
  --holiday:#c4d52f;
  --rule:#8f9496;
  --ink:#1f1f1f;
  --accent:#c8d43a;
  --white:#ffffff;
}
*{margin:0;padding:0;box-sizing:border-box}
html,body{width:1200px;height:849px;overflow:hidden}
body{position:relative;font-family:"Roboto Condensed",Arial,sans-serif;color:var(--ink)}
.backdrop{position:absolute;inset:0;
  background:
   radial-gradient(ellipse at 88% 50%, rgba(216,100,30,.85) 0%, rgba(216,100,30,0) 22%),
   radial-gradient(ellipse at 95% 80%, rgba(70,110,60,.9) 0%, rgba(70,110,60,0) 25%),
   linear-gradient(120deg,#6f7a72 0%,var(--smoke-mid) 30%,var(--smoke-dark) 60%,#3a3f3e 100%);}
.months{position:absolute;left:18px;top:14px;width:932px;display:grid;grid-template-columns:repeat(12,74px);column-gap:4.36px}
.months h2{font-family:"Oswald",sans-serif;font-weight:700;font-size:15px;color:var(--white);text-align:center;letter-spacing:.2px}
.calendar{position:absolute;left:18px;top:47px;width:932px;height:577px;display:grid;grid-template-columns:repeat(12,74px);column-gap:4.36px}
.month{list-style:none;background:var(--paper);padding-top:2px}
.month li{position:relative;height:18.5px;line-height:17px;font-size:9.5px;padding-left:4px;margin:0 2px;border-bottom:1px solid var(--rule)}
.month li.we{background:var(--weekend)}
.month li.hol{background:var(--holiday)}
.month li i{position:absolute;right:2px;top:50%;transform:translateY(-50%);font-style:normal;font-size:5px;line-height:5.5px;text-align:right;max-width:40px}
.month li b{position:absolute;right:1px;top:-6px;font-weight:400;font-size:5px;line-height:5px}
.year{position:absolute;left:975px;top:36px;font-family:"Oswald",sans-serif;font-weight:700;font-size:62px;line-height:70px;color:var(--white);letter-spacing:2px}
.brand{position:absolute;left:980px;top:115px;width:190px;height:60px;display:flex;align-items:center;gap:10px}
.brand .square{width:34px;height:34px;background:var(--accent)}
.brand span{font-family:"Oswald",sans-serif;font-weight:700;font-size:40px;color:var(--white)}
.web{position:absolute;left:994px;top:182px;font-family:"Oswald",sans-serif;font-weight:700;font-size:15px;color:var(--white);letter-spacing:.5px}
.photo{position:absolute}
.photo-accident{left:0;top:624px;width:470px;height:225px;background:linear-gradient(160deg,#3b3e3c,#8a5a2a 55%,#b6652a)}
.photo-camera{left:225px;top:590px;width:250px;height:259px;background:linear-gradient(180deg,rgba(60,60,60,.0),#4b4b48 20%,#c9d23a 70%,#8e9a2a)}
.photo-fire{left:470px;top:624px;width:330px;height:225px;background:linear-gradient(135deg,#2a2a28,#c55a1a 50%,#e8902c 70%,#3a2a22)}
.photo-rescue{left:955px;top:624px;width:245px;height:225px;background:linear-gradient(180deg,#71806f,#4d6b45 50%,#8aa862)}
.infobox{position:absolute;left:797px;top:628px;width:158px;height:221px;background:var(--accent);color:var(--white);text-align:center;font-weight:700;padding-top:15px}
.infobox h3{font-size:11.5px;line-height:14px}
.infobox p{font-size:7.5px;font-weight:400;margin-top:2px}
.infobox .call{font-size:11px;line-height:14px;margin-top:10px}
.infobox .num{font-size:14px;margin-top:2px}
.infobox .small{font-size:5.5px;font-weight:400;margin-top:3px}
.infobox .sms{font-size:11px;line-height:14px;margin-top:10px}
</style>
</head>
<body>
<div class="backdrop" role="img" aria-label="Hintergrundfoto: Rauchwolken über einem brennenden Waldstück mit Feuerwehrdrehleiter an einer Brücke"></div>

<div class="months">
<h2>JANUAR</h2><h2>FEBRUAR</h2><h2>MÄRZ</h2><h2>APRIL</h2><h2>MAI</h2><h2>JUNI</h2><h2>JULI</h2><h2>AUGUST</h2><h2>SEPTEMBER</h2><h2>OKTOBER</h2><h2>NOVEMBER</h2><h2>DEZEMBER</h2>
</div>

<div class="calendar">
<ul class="month">
<li class="hol">01 Di<i>Neujahr</i><b>1</b></li><li>02 Mi</li><li>03 Do</li><li>04 Fr</li><li class="we">05 Sa</li><li class="we">06 So<i>Heilige Drei Könige</i></li><li>07 Mo<b>2</b></li><li>08 Di</li><li>09 Mi</li><li>10 Do</li><li>11 Fr</li><li class="we">12 Sa</li><li class="we">13 So</li><li>14 Mo<b>3</b></li><li>15 Di</li><li>16 Mi</li><li>17 Do</li><li>18 Fr</li><li class="we">19 Sa</li><li class="we">20 So</li><li>21 Mo<b>4</b></li><li>22 Di</li><li>23 Mi</li><li>24 Do</li><li>25 Fr</li><li class="we">26 Sa</li><li class="we">27 So</li><li>28 Mo<b>5</b></li><li>29 Di</li><li>30 Mi</li><li>31 Do</li>
</ul>
<ul class="month">
<li>01 Fr</li><li class="we">02 Sa</li><li class="we">03 So</li><li>04 Mo<b>6</b></li><li>05 Di</li><li>06 Mi</li><li>07 Do</li><li>08 Fr</li><li class="we">09 Sa</li><li class="we">10 So</li><li>11 Mo<b>7</b></li><li>12 Di</li><li>13 Mi</li><li>14 Do<i>Valentinstag</i></li><li>15 Fr</li><li class="we">16 Sa</li><li class="we">17 So</li><li>18 Mo<b>8</b></li><li>19 Di</li><li>20 Mi</li><li>21 Do</li><li>22 Fr</li><li class="we">23 Sa</li><li class="we">24 So</li><li>25 Mo<b>9</b></li><li>26 Di</li><li>27 Mi</li><li>28 Do<i>Weiberfastnacht</i></li>
</ul>
<ul class="month">
<li>01 Fr<i>Frühlingsanfang</i></li><li class="we">02 Sa</li><li class="we">03 So</li><li>04 Mo<i>Rosenmontag</i><b>10</b></li><li>05 Di<i>Fastnacht</i></li><li>06 Mi<i>Aschermittwoch</i></li><li>07 Do</li><li>08 Fr</li><li class="we">09 Sa</li><li class="we">10 So</li><li>11 Mo<b>11</b></li><li>12 Di</li><li>13 Mi</li><li>14 Do</li><li>15 Fr</li><li class="we">16 Sa</li><li class="we">17 So</li><li>18 Mo<b>12</b></li><li>19 Di</li><li>20 Mi<i>Frühlingsanfang</i></li><li>21 Do</li><li>22 Fr</li><li class="we">23 Sa</li><li class="we">24 So</li><li>25 Mo<b>13</b></li><li>26 Di</li><li>27 Mi</li><li>28 Do</li><li>29 Fr</li><li class="we">30 Sa</li><li class="we">31 So<i>Beginn der Sommerzeit</i></li>
</ul>
<ul class="month">
<li>01 Mo<b>14</b></li><li>02 Di</li><li>03 Mi</li><li>04 Do</li><li>05 Fr</li><li class="we">06 Sa</li><li class="we">07 So</li><li>08 Mo<b>15</b></li><li>09 Di</li><li>10 Mi</li><li>11 Do</li><li>12 Fr</li><li class="we">13 Sa</li><li class="we">14 So<i>Palmsonntag</i></li><li>15 Mo<b>16</b></li><li>16 Di</li><li>17 Mi</li><li>18 Do</li><li class="hol">19 Fr<i>Karfreitag</i></li><li class="we">20 Sa</li><li class="hol">21 So<i>Ostersonntag</i></li><li class="hol">22 Mo<i>Ostermontag</i><b>17</b></li><li>23 Di</li><li>24 Mi</li><li>25 Do</li><li>26 Fr</li><li class="we">27 Sa</li><li class="we">28 So</li><li>29 Mo<b>18</b></li><li>30 Di</li>
</ul>
<ul class="month">
<li class="hol">01 Mi<i>Tag der Arbeit</i></li><li>02 Do</li><li>03 Fr</li><li class="we">04 Sa</li><li class="we">05 So</li><li>06 Mo<b>19</b></li><li>07 Di</li><li>08 Mi</li><li>09 Do</li><li>10 Fr</li><li class="we">11 Sa</li><li class="we">12 So<i>Muttertag</i></li><li>13 Mo<b>20</b></li><li>14 Di</li><li>15 Mi</li><li>16 Do</li><li>17 Fr</li><li class="we">18 Sa</li><li class="we">19 So</li><li>20 Mo<b>21</b></li><li>21 Di</li><li>22 Mi</li><li>23 Do</li><li>24 Fr</li><li class="we">25 Sa</li><li class="we">26 So</li><li>27 Mo<b>22</b></li><li>28 Di</li><li>29 Mi</li><li class="hol">30 Do<i>Vatertag Himmelfahrt</i></li><li>31 Fr</li>
</ul>
<ul class="month">
<li class="we">01 Sa</li><li class="we">02 So</li><li>03 Mo<b>23</b></li><li>04 Di</li><li>05 Mi</li><li>06 Do</li><li>07 Fr</li><li class="we">08 Sa</li><li class="hol">09 So<i>Pfingstsonntag</i></li><li class="hol">10 Mo<i>Pfingstmontag</i><b>24</b></li><li>11 Di</li><li>12 Mi</li><li>13 Do</li><li>14 Fr</li><li class="we">15 Sa</li><li class="we">16 So</li><li>17 Mo<b>25</b></li><li>18 Di</li><li>19 Mi</li><li>20 Do<i>Fronleichnam</i></li><li>21 Fr<i>Sommeranfang</i></li><li class="we">22 Sa</li><li class="we">23 So</li><li>24 Mo<b>26</b></li><li>25 Di</li><li>26 Mi</li><li>27 Do</li><li>28 Fr</li><li class="we">29 Sa</li><li class="we">30 So</li>
</ul>
<ul class="month">
<li>01 Mo<b>27</b></li><li>02 Di</li><li>03 Mi</li><li>04 Do</li><li>05 Fr</li><li class="we">06 Sa</li><li class="we">07 So</li><li>08 Mo<b>28</b></li><li>09 Di</li><li>10 Mi</li><li>11 Do</li><li>12 Fr</li><li class="we">13 Sa</li><li class="we">14 So</li><li>15 Mo<b>29</b></li><li>16 Di</li><li>17 Mi</li><li>18 Do</li><li>19 Fr</li><li class="we">20 Sa</li><li class="we">21 So</li><li>22 Mo<b>30</b></li><li>23 Di</li><li>24 Mi</li><li>25 Do</li><li>26 Fr</li><li class="we">27 Sa</li><li class="we">28 So</li><li>29 Mo<b>31</b></li><li>30 Di</li><li>31 Mi</li>
</ul>
<ul class="month">
<li>01 Do</li><li>02 Fr</li><li class="we">03 Sa</li><li class="we">04 So</li><li>05 Mo<b>32</b></li><li>06 Di</li><li>07 Mi</li><li>08 Do</li><li>09 Fr</li><li class="we">10 Sa</li><li class="we">11 So</li><li>12 Mo<b>33</b></li><li>13 Di</li><li>14 Mi</li><li>15 Do<i>Mariä Himmelfahrt</i></li><li>16 Fr</li><li class="we">17 Sa</li><li class="we">18 So</li><li>19 Mo<b>34</b></li><li>20 Di</li><li>21 Mi</li><li>22 Do</li><li>23 Fr</li><li class="we">24 Sa</li><li class="we">25 So</li><li>26 Mo<b>35</b></li><li>27 Di</li><li>28 Mi</li><li>29 Do</li><li>30 Fr</li><li class="we">31 Sa</li>
</ul>
<ul class="month">
<li class="we">01 So<i>Herbstanfang</i></li><li>02 Mo<b>36</b></li><li>03 Di</li><li>04 Mi</li><li>05 Do</li><li>06 Fr</li><li class="we">07 Sa</li><li class="we">08 So</li><li>09 Mo<b>37</b></li><li>10 Di</li><li>11 Mi</li><li>12 Do</li><li>13 Fr</li><li class="we">14 Sa</li><li class="we">15 So</li><li>16 Mo<b>38</b></li><li>17 Di</li><li>18 Mi</li><li>19 Do</li><li>20 Fr</li><li class="we">21 Sa</li><li class="we">22 So</li><li>23 Mo<b>39</b></li><li>24 Di</li><li>25 Mi</li><li>26 Do</li><li>27 Fr</li><li class="we">28 Sa</li><li class="we">29 So</li><li>30 Mo<b>40</b></li>
</ul>
<ul class="month">
<li>01 Di</li><li>02 Mi</li><li class="hol">03 Do<i>Tag der Deutschen Einheit</i></li><li>04 Fr</li><li class="we">05 Sa</li><li class="we">06 So<i>Erntedankfest</i></li><li>07 Mo<b>41</b></li><li>08 Di</li><li>09 Mi</li><li>10 Do</li><li>11 Fr</li><li class="we">12 Sa</li><li class="we">13 So</li><li>14 Mo<b>42</b></li><li>15 Di</li><li>16 Mi</li><li>17 Do</li><li>18 Fr</li><li class="we">19 Sa</li><li class="we">20 So</li><li>21 Mo<b>43</b></li><li>22 Di</li><li>23 Mi</li><li>24 Do</li><li>25 Fr</li><li class="we">26 Sa</li><li class="we">27 So<i>Ende der Sommerzeit</i></li><li>28 Mo<b>44</b></li><li>29 Di</li><li>30 Mi</li><li>31 Do<i>Halloween Reformationstag</i></li>
</ul>
<ul class="month">
<li>01 Fr<i>Allerheiligen</i></li><li class="we">02 Sa</li><li class="we">03 So</li><li>04 Mo<b>45</b></li><li>05 Di</li><li>06 Mi</li><li>07 Do</li><li>08 Fr</li><li class="we">09 Sa</li><li class="we">10 So</li><li>11 Mo<i>St. Martin</i><b>46</b></li><li>12 Di</li><li>13 Mi</li><li>14 Do</li><li>15 Fr</li><li class="we">16 Sa</li><li class="we">17 So<i>Volkstrauertag</i></li><li>18 Mo<b>47</b></li><li>19 Di</li><li>20 Mi<i>Buß- und Bettag</i></li><li>21 Do</li><li>22 Fr</li><li class="we">23 Sa</li><li class="we">24 So<i>Totensonntag</i></li><li>25 Mo<b>48</b></li><li>26 Di</li><li>27 Mi</li><li>28 Do</li><li>29 Fr</li><li class="we">30 Sa</li>
</ul>
<ul class="month">
<li class="hol">01 So<i>1. Advent</i></li><li>02 Mo<b>49</b></li><li>03 Di</li><li>04 Mi</li><li>05 Do</li><li>06 Fr</li><li class="we">07 Sa</li><li class="we">08 So<i>2. Advent</i></li><li>09 Mo<b>50</b></li><li>10 Di</li><li>11 Mi</li><li>12 Do</li><li>13 Fr</li><li class="we">14 Sa</li><li class="we">15 So<i>3. Advent</i></li><li>16 Mo<b>51</b></li><li>17 Di</li><li>18 Mi</li><li>19 Do</li><li>20 Fr</li><li class="we">21 Sa</li><li class="we">22 So<i>Winteranfang 4. Advent</i></li><li>23 Mo<b>52</b></li><li>24 Di<i>Heiligabend</i></li><li class="hol">25 Mi<i>1. Weihnachts-feiertag</i></li><li class="hol">26 Do<i>2. Weihnachts-feiertag</i></li><li>27 Fr</li><li class="we">28 Sa</li><li class="we">29 So</li><li>30 Mo<b>1</b></li><li class="hol">31 Di<i>Silvester</i></li>
</ul>
</div>

<div class="year">2019</div>
<div class="brand"><div class="square"></div><span>PRESSE7</span></div>
<div class="web">WWW.PRESSE7.DE</div>

<div class="photo photo-accident" role="img" aria-label="Foto: Verkehrsunfall mit umgestürztem Lkw und Feuerwehrfahrzeugen bei Nacht"></div>
<div class="photo photo-fire" role="img" aria-label="Foto: Feuerwehrleute vor einem lodernden Großbrand"></div>
<div class="photo photo-camera" role="img" aria-label="Freigestelltes Foto: Kameramann in Warnweste mit Videokamera vor einem verunfallten Lkw"></div>
<div class="photo photo-rescue" role="img" aria-label="Foto: Rettungshubschrauber und Rettungswagen auf einer Wiese, dahinter eine überflutete Straße"></div>

<aside class="infobox">
  <h3>Kenntnis von<br>aktuellen Ereignissen?</h3>
  <p>Unfälle, Brände oder Polizeieinsätze.</p>
  <div class="call">Rufen Sie uns an!<br>24h-Telefon</div>
  <div class="num">0800 / 31 46 270</div>
  <div class="small">(Aus dem dt. Festnetz und Mobil kostenlos)</div>
  <div class="sms">Oder schreiben<br>Sie uns eine SMS</div>
  <div class="num">0171 / 58 62 917</div>
</aside>
</body>
</html>
```